A billboard for Harlow Ridge Construction size 36.5’ x 14.5’

Hi guys. We are purchasing a billboard and are looking for a design (size 36.5’ x 14.5’). Our slogan is "Quality you deserve, service you can count on". The goal of this billboard is brand recognition primarily letting people know we do roofs. Attached are logos that can be used if needed. Not necessarily all of them need to be used.

Target Market(s)

Residents in the local areas needing or thinking about a roof replacement

Industry/Entity Type

Roofing

Requirements
Must have
• Logo and services (roof replacement, gutters, siding, and snow removal)
Nice to have
• take a look at our website for ideas www.harlowridgeconstruction.example

```html
<!DOCTYPE html>
<html lang="en">
<head>
<meta charset="utf-8">
<title>Harlow Ridge Construction Billboard</title>
<link rel="stylesheet" href="https://fonts.googleapis.com/css2?family=Montserrat:wght@300;500;600&family=Playfair+Display:wght@400&display=swap">
<style>
  :root {
    --canvas-bg: #a7a7a7;
    --panel-white: #ffffff;
    --band-black: #0b0b0b;
    --accent-red: #e4161b;
    --ink: #111111;
    --photo-sky: #9fc3e6;
    --photo-roof: #6f6a63;
    --photo-brick: #8c7a6c;
    --photo-ground: #5d6b4a;
    --badge-blue: #1f6e8c;
    --badge-dark: #2a2a2a;
    --badge-tan: #c9b48e;
  }
  * { margin: 0; padding: 0; box-sizing: border-box; }
  html, body {
    width: 1035px;
    height: 1200px;
    overflow: hidden;
    background: var(--canvas-bg);
  }
  .billboard {
    position: absolute;
    left: 0;
    top: 394px;
    width: 1035px;
    height: 411px;
    overflow: hidden;
    font-family: "Montserrat", Arial, sans-serif;
  }
  .billboard-art {
    position: absolute;
    inset: 0;
    display: block;
  }
  .brand-name {
    position: absolute;
    left: 620px;
    top: 66px;
    width: 320px;
    text-align: center;
    font-family: "Playfair Display", Georgia, serif;
    font-weight: 400;
    font-size: 31px;
    line-height: 34px;
    color: var(--ink);
  }
  .slogan {
    position: absolute;
    text-align: center;
    white-space: nowrap;
  }
  .slogan-primary {
    left: 563px;
    width: 420px;
    top: 183px;
    font-weight: 300;
    font-size: 27.5px;
    letter-spacing: 0.5px;
    color: var(--accent-red);
  }
  .slogan-secondary {
    left: 523px;
    width: 500px;
    top: 217px;
    font-weight: 600;
    font-size: 30.5px;
    letter-spacing: 0.4px;
    color: var(--panel-white);
  }
  .service-list {
    position: absolute;
    list-style: none;
    top: 294px;
    font-weight: 500;
    font-size: 23.5px;
    line-height: 35px;
    color: var(--ink);
    white-space: nowrap;
  }
  .service-list li::before {
    content: "\2022";
    margin-right: 5px;
  }
  .service-list--main { left: 578px; }
  .service-list--extra { left: 873px; }
</style>
</head>
<body>
  <section class="billboard" aria-label="Harlow Ridge Construction billboard">
    <svg class="billboard-art" viewBox="0 0 1035 411" width="1035" height="411">
      <defs>
        <linearGradient id="houseTones" x1="0" y1="0" x2="0" y2="1">
          <stop offset="0" stop-color="#9fc3e6"/>
          <stop offset="0.18" stop-color="#6f6a63"/>
          <stop offset="0.45" stop-color="#6f6a63"/>
          <stop offset="0.6" stop-color="#8c7a6c"/>
          <stop offset="0.92" stop-color="#8c7a6c"/>
          <stop offset="1" stop-color="#5d6b4a"/>
        </linearGradient>
      </defs>

      <rect class="house-photo" role="img" aria-label="Photo of a large two-storey brick house with a new shingle roof" x="0" y="0" width="620" height="411" fill="url(#houseTones)"/>

      <polygon class="panel-upper" points="527,0 1035,0 1035,166 596,166" fill="var(--panel-white)"/>
      <polygon class="stripe-upper" points="515,0 527,0 596,166 584,166" fill="var(--accent-red)"/>

      <polygon class="slogan-band" points="472,166 1035,166 1035,275 517,275" fill="var(--band-black)"/>
      <polygon class="panel-lower" points="517,275 1035,275 1035,411 573,411" fill="var(--panel-white)"/>
      <polygon class="stripe-lower" points="462,166 472,166 573,411 563,411" fill="var(--accent-red)"/>

      <g class="partner-badges">
        <circle class="badge badge-shingle" cx="68" cy="364" r="30" fill="var(--badge-dark)"/>
        <rect class="badge badge-protect" x="106" y="346" width="30" height="44" fill="var(--badge-tan)"/>
        <rect class="badge badge-accredited" x="171" y="353" width="111" height="42" fill="var(--badge-blue)"/>
        <rect class="badge-mark" x="177" y="359" width="30" height="30" fill="var(--panel-white)"/>
      </g>
    </svg>

    <h1 class="brand-name">Harlow Ridge<br>Construction</h1>

    <p class="slogan slogan-primary">QUALITY YOU DESERVE</p>
    <p class="slogan slogan-secondary">SERVICE YOU CAN COUNT ON</p>

    <ul class="service-list service-list--main">
      <li>Roof Replacement</li>
      <li>Snow Removal</li>
    </ul>
    <ul class="service-list service-list--extra">
      <li>Gutters</li>
      <li>Siding</li>
    </ul>
  </section>
</body>
</html>
```